Estate Agent/Real Estate valuation tool

We need a design for our our new estate agent valuation tool.

The tool allows users to book a valuation of their house/property with the estate agent, after they choose there property they can then complete their details and choose a booking time.

The mock up of the design we want is attached to this project.(Main Screen)

This also needs to be responsive so the design is easy to use on a mobile device.

Target Market(s)

estate agents

Industry/Entity Type

Real Estate Agent

Number of Pages Required

1 page

Requirements
Must have
• Section 2 and 3 greyed out when user is on step 1
• Section 1 and 3 greyed out when user is on step 2
• Section 1 and 2 greyed out when the user is on step 3
• *** Design must be shown for mobile/ipad and desktop
Nice to have
• Clean and Simple
Should not have
• Dark colours

```html
<!DOCTYPE html>
<html lang="en">
<head>
<meta charset="utf-8">
<title>Real Estate Valuation – Book Your Valuation Online</title>
<link rel="stylesheet" href="https://fonts.googleapis.com/css2?family=Noto+Serif:wght@400;700&family=Open+Sans:wght@700&display=swap">
<style>
  :root{
    --page:#ffffff;
    --ink:#222222;
    --orange:#f7941d;
    --orange-dark:#e67e0b;
    --green:#3bab4a;
    --panel-light:#f3f3f3;
    --panel-line:#cfcfcf;
    --panel-dark:#1e1e1e;
    --ribbon-dark:#141414;
    --field:#ffffff;
    --field-line:#d4d4d4;
    --field-text:#555555;
    --button-grey:#4d4d4d;
    --band:#ececec;
    --time-chip:#e2e2e2;
  }
  *{box-sizing:border-box;margin:0;padding:0}
  html,body{width:1200px;height:4894px;overflow:hidden;background:var(--page)}
  .screen{
    position:absolute;left:0;top:0;width:320px;height:1305px;
    transform:scale(3.75);transform-origin:0 0;
    font-family:"Noto Serif",Georgia,serif;color:var(--ink);
  }
  .abs{position:absolute}

  .brand{left:0;top:20px;width:320px;height:125px;text-align:center}
  .brand-mark{position:absolute;left:148px;top:38px;width:24px;height:24px;background:var(--orange);border-radius:50%}
  .brand-name{position:absolute;left:0;right:0;top:78px;font-size:20px;font-weight:700;letter-spacing:-.2px}

  .band{left:0;top:148px;width:320px;height:50px;background:linear-gradient(#f2f2f2,var(--band));
    display:flex;align-items:center;justify-content:center;
    font-family:"Open Sans",Arial,sans-serif;font-weight:700;font-size:15px;color:var(--orange)}

  .panel{left:11px;width:297px}
  .panel--light{top:224px;height:304px;background:var(--panel-light);border:1px solid var(--panel-line)}
  .panel--dark{background:var(--panel-dark);border-radius:3px;left:10px;width:299px}
  .panel--details{top:539px;height:258px}
  .panel--time{top:811px;height:479px}

  .ribbon{position:absolute;left:0;height:41px;display:flex;align-items:center;color:#fff;font-size:19px}
  .ribbon svg{position:absolute;left:0;top:0}
  .ribbon span{position:relative}
  .step-no{position:relative;width:28px;height:28px;border-radius:50%;margin:0 9px 0 12px;
    display:flex;align-items:center;justify-content:center;font-size:17px;font-weight:700}
  .ribbon--dark .step-no{background:var(--orange);color:#fff}
  .ribbon--orange .step-no{background:#fff;color:var(--orange)}
  .ribbon--orange span.title{text-shadow:0 1px 1px rgba(0,0,0,.25)}

  .field{position:absolute;left:9px;width:280px;height:38px;background:var(--field);border:1px solid var(--field-line);
    border-radius:2px;display:flex;align-items:center;padding-left:10px;font-size:13px;color:var(--field-text)}
  .search-btn{position:absolute;left:250px;top:68px;width:38px;height:38px;background:var(--green);
    display:flex;align-items:center;justify-content:center;border-radius:0 2px 2px 0}
  .btn{position:absolute;left:9px;width:280px;height:38px;display:flex;align-items:center;justify-content:center;
    color:#fff;font-weight:700;font-size:15px;letter-spacing:.3px}
  .btn--go{background:var(--green)}
  .btn--grey{background:var(--button-grey)}

  .day{position:absolute;height:44px;background:#fff;display:flex;align-items:center;justify-content:center;
    font-size:11px;color:#111;border-radius:2px}
  .day--active{background:var(--green);color:#fff}

  .slot{position:absolute;left:10px;width:281px;height:38px;background:#fff;border-radius:2px;
    display:flex;align-items:center;padding-left:7px;font-size:12px;color:#444}
  .slot::after{content:"";position:absolute;left:212px;top:0;bottom:0;width:1px;background:#d6d6d6}
  .slot-time{position:absolute;right:5px;top:4px;width:53px;height:30px;background:var(--time-chip);border-radius:2px;
    display:flex;align-items:center;justify-content:center;font-weight:700;font-size:15px;color:#222}
</style>
</head>
<body>
<main class="screen">
  <header class="brand abs">
    <div class="brand-mark"></div>
    <h1 class="brand-name">Real Estate Valuation</h1>
  </header>

  <div class="band abs">BOOK YOUR VALUATION ONLINE</div>

  <section class="panel panel--light abs">
    <div class="ribbon ribbon--dark" style="top:8px;width:235px">
      <svg width="235" height="41" viewBox="0 0 235 41"><polygon points="0,0 210,0 235,20.5 210,41 0,41" fill="var(--ribbon-dark)"/></svg>
      <div class="step-no">01</div><span>Property Details</span>
    </div>
    <div class="field" style="top:68px;width:242px;border-radius:2px 0 0 2px">125648</div>
    <div class="search-btn">
      <svg width="20" height="20" viewBox="0 0 20 20" fill="none" stroke="#fff" stroke-width="2"><circle cx="8.5" cy="8.5" r="6.5"/><line x1="13.5" y1="13.5" x2="18.5" y2="18.5"/></svg>
    </div>
    <div class="field" style="top:114px">123 Test Street</div>
    <div class="field" style="top:160px">Test City</div>
    <div class="field" style="top:206px">Test Country</div>
    <div class="btn btn--go" style="top:251px">PROCEED</div>
  </section>

  <section class="panel panel--dark panel--details abs">
    <div class="ribbon ribbon--orange" style="top:9px;width:218px">
      <svg width="218" height="42" viewBox="0 0 218 42"><defs><linearGradient id="rg1" x1="0" y1="0" x2="0" y2="1"><stop offset="0" stop-color="#fba53a"/><stop offset="1" stop-color="var(--orange-dark)"/></linearGradient></defs><polygon points="0,0 196,0 218,21 196,42 0,42" fill="url(#rg1)"/></svg>
      <div class="step-no">02</div><span class="title">Your Details</span>
    </div>
    <div class="field" style="top:70px;left:10px">Your Name:</div>
    <div class="field" style="top:116px;left:10px">Your Email:</div>
    <div class="field" style="top:162px;left:10px">Yout Contact No.</div>
    <div class="btn btn--grey" style="top:209px;left:10px">PROCEED</div>
  </section>

  <section class="panel panel--dark panel--time abs">
    <div class="ribbon ribbon--orange" style="top:9px;width:258px">
      <svg width="258" height="42" viewBox="0 0 258 42"><defs><linearGradient id="rg2" x1="0" y1="0" x2="0" y2="1"><stop offset="0" stop-color="#fba53a"/><stop offset="1" stop-color="var(--orange-dark)"/></linearGradient></defs><polygon points="0,0 236,0 258,21 236,42 0,42" fill="url(#rg2)"/></svg>
      <div class="step-no">03</div><span class="title">Appointment Time</span>
    </div>

    <div class="day" style="left:10px;top:72px;width:56px">Today</div>
    <div class="day day--active" style="left:78px;top:72px;width:77px">Tomorrow</div>
    <div class="day" style="left:166px;top:72px;width:57px">Mon-30th</div>
    <div class="day" style="left:234px;top:72px;width:57px">Tue - 1st</div>
    <div class="day" style="left:10px;top:126px;width:57px">Wed - 2nd</div>
    <div class="day" style="left:78px;top:126px;width:58px">Thus - 4th</div>
    <div class="day" style="left:147px;top:126px;width:57px">Fri - 5th</div>

    <div class="slot" style="top:191px">Sunday 29th November<span class="slot-time">08:30</span></div>
    <div class="slot" style="top:237px">Sunday 29th November<span class="slot-time">10:30</span></div>
    <div class="slot" style="top:283px">Sunday 29th November<span class="slot-time">12:30</span></div>
    <div class="slot" style="top:329px">Sunday 29th November<span class="slot-time">14:30</span></div>
    <div class="slot" style="top:375px">Sunday 29th November<span class="slot-time">16:30</span></div>

    <div class="btn btn--grey" style="top:427px;left:10px;width:280px;height:37px">CONFIRM BOOKING</div>
  </section>
</main>
</body>
</html>
```